Oil and Gas Company: Letterhead Design

In short we need a professional company letterhead designed for our Oil and Gas company.

We would like to keep the design simple and professional. Letterhead to include the company logo and color scheme, front page and continuation pages.

For reference, see attached logo below with our company logo and color scheme.

Target Market(s)

Oil & Gas Market

Industry/Entity Type

Oil And Gas

Font styles to use
Sans Serif

Requirements
Must have
• Letterhead must contain a front page & continuation page.
• Must be simple and professional in design.
• Follow our logo and color scheme.
Nice to have
• I would like to have the logo embedded in the bottom right hand portion of the page to provide some depth into the letterhead.

```html
<!DOCTYPE html>
<html lang="en">
<head>
<meta charset="utf-8">
<title>Crestline Energy Services – Letterhead and Continuation Sheet</title>
<link rel="stylesheet" href="https://fonts.googleapis.com/css2?family=Montserrat:wght@400&family=Tinos&display=swap">
<style>
  :root {
    --board-light: #e8e8e8;
    --board-dark: #7b7b7b;
    --paper: #ffffff;
    --navy: #1b2a44;
    --brand-blue: #1f4f9e;
    --brand-red: #e0262b;
    --contact-text: #555a63;
    --accent-peach: #f4b79c;
    --accent-lavender: #aab1da;
    --caption: #ffffff;
  }
  * { box-sizing: border-box; margin: 0; padding: 0; }
  html, body { width: 1200px; height: 792px; overflow: hidden; }
  body {
    background: radial-gradient(ellipse 60% 75% at 50% 50%, var(--board-light) 0%, #bdbdbd 50%, var(--board-dark) 100%);
    position: relative;
    font-family: "Montserrat", sans-serif;
  }
  .sheet {
    position: absolute;
    top: 67px;
    width: 482px;
    height: 623px;
    background: var(--paper);
    overflow: hidden;
  }
  .sheet--letterhead { left: 124px; }
  .sheet--continuation { left: 645px; }

  .corner-accent {
    position: absolute;
    left: 0;
    top: 0;
    width: 190px;
    height: 218px;
    background:
      radial-gradient(ellipse 90% 80% at 30% 25%, rgba(170,177,218,0.55) 0%, rgba(170,177,218,0) 60%),
      linear-gradient(135deg, rgba(244,183,156,0.6) 0%, rgba(244,183,156,0.25) 45%, rgba(244,183,156,0) 75%);
    clip-path: polygon(0 0, 100% 0, 62% 60%, 45% 100%, 0 60%);
  }

  .brand-name {
    position: absolute;
    right: 36px;
    bottom: 22px;
    width: 150px;
    text-align: center;
    color: var(--navy);
    font-size: 11px;
    line-height: 12px;
    letter-spacing: 0.5px;
  }
  .brand-name .brand-mark {
    display: block;
    width: 18px;
    height: 18px;
    margin: 0 auto 10px;
    background: var(--brand-blue);
  }

  .contact-list {
    position: absolute;
    left: 29px;
    top: 562px;
    list-style: none;
  }
  .contact-list li {
    display: flex;
    align-items: center;
    height: 15px;
    font-size: 9px;
    color: var(--contact-text);
  }
  .contact-list svg {
    width: 11px;
    height: 11px;
    margin-right: 6px;
    flex: none;
  }

  .caption {
    position: absolute;
    top: 708px;
    width: 482px;
    text-align: center;
    font-family: "Tinos", serif;
    font-size: 29px;
    color: var(--caption);
  }
  .caption--letterhead { left: 80px; width: 482px; }
  .caption--continuation { left: 645px; }
</style>
</head>
<body>

  <section class="sheet sheet--letterhead" aria-label="Letterhead front page">
    <div class="corner-accent" role="img" aria-label="Faint peach and lavender corner accent"></div>

    <ul class="contact-list">
      <li>
        <svg viewBox="0 0 12 12" aria-hidden="true">
          <rect x="2" y="0.5" width="8" height="11" rx="1" fill="var(--brand-blue)"/>
          <rect x="3.3" y="1.8" width="5.4" height="3" fill="#fff"/>
          <g fill="#fff"><rect x="3.3" y="6" width="1.3" height="1.2"/><rect x="5.35" y="6" width="1.3" height="1.2"/><rect x="7.4" y="6" width="1.3" height="1.2"/><rect x="3.3" y="8.2" width="1.3" height="1.2"/><rect x="5.35" y="8.2" width="1.3" height="1.2"/><rect x="7.4" y="8.2" width="1.3" height="1.2"/></g>
        </svg>
        number
      </li>
      <li>
        <svg viewBox="0 0 12 12" aria-hidden="true">
          <rect x="0.5" y="2" width="11" height="8" fill="var(--brand-blue)"/>
          <path d="M1 2.5 L6 6.8 L11 2.5 M1 9.5 L4.5 5.8 M11 9.5 L7.5 5.8" stroke="#fff" stroke-width="0.9" fill="none"/>
        </svg>
        name@crestlineenergyservices.com
      </li>
      <li>
        <svg viewBox="0 0 12 12" aria-hidden="true">
          <circle cx="6" cy="6" r="5.5" fill="var(--brand-blue)"/>
          <g stroke="#fff" stroke-width="0.7" fill="none">
            <ellipse cx="6" cy="6" rx="2.3" ry="5.5"/>
            <line x1="0.5" y1="6" x2="11.5" y2="6"/>
            <line x1="1.3" y1="3.4" x2="10.7" y2="3.4"/>
            <line x1="1.3" y1="8.6" x2="10.7" y2="8.6"/>
          </g>
        </svg>
        www.crestlineenergyservices.com
      </li>
    </ul>

    <p class="brand-name"><span class="brand-mark"></span>CRESTLINE<br>ENERGY SERVICES</p>
  </section>

  <section class="sheet sheet--continuation" aria-label="Continuation sheet">
    <div class="corner-accent" role="img" aria-label="Faint peach and lavender corner accent"></div>
    <p class="brand-name"><span class="brand-mark"></span>CRESTLINE<br>ENERGY SERVICES</p>
  </section>

  <p class="caption caption--letterhead">Letterhead</p>
  <p class="caption caption--continuation">Continuation sheet</p>

</body>
</html>
```